Business Card Design for Loft Pictures

Hi we need a business card designed for a new aerial photography business we have started, we use UAV Drones to take photos for corporate, events, real estate, local government etc , the business name is Loft Pictures Australia, we have a facebook page that might help you come up with some designs - https://www.facebook.com/loftpicturesaustralia

We need to have and editable AI file so that we can use different names and contact details. details for one of the cards as follow:

Ned Harrow
phone: 03 5521 4736
Mobile: 0431 957 284
email: ned@loftpicturez.example
web: www.loftpictures.example

have now changed: Designer Payment:Committed

Target Market(s)

We are a Aerial Photography business using Drones and UAV

Industry/Entity Type

Business

Logo Text

Loft Pictures Australia

Requirements
Must have
• Colors to match logo and be part of Loft Pictures Brand

```html
<!DOCTYPE html>
<html lang="en">
<head>
<meta charset="utf-8">
<title>Loft Pictures Australia – Business Card</title>
<link rel="stylesheet" href="https://fonts.googleapis.com/css2?family=Exo+2:wght@700&family=Open+Sans:wght@700&display=swap">
<style>
  :root {
    --page-bg: #e9eaec;
    --sky-deep: #1fa3e2;
    --sky-mid: #55bdf0;
    --sky-light: #bfe6fb;
    --card-white: #eeeff1;
    --ink: #222326;
    --pill-top: #e4e5e7;
    --pill-bottom: #9c9ea2;
    --contact-text: #ffffff;
  }
  * { box-sizing: border-box; margin: 0; padding: 0; }
  html, body {
    width: 1200px; height: 900px; overflow: hidden;
    background: var(--page-bg);
  }
  .canvas {
    position: relative; width: 1200px; height: 900px;
  }
  .card {
    position: absolute; left: 285px;
    width: 630px; height: 360px;
    overflow: hidden;
    box-shadow: 0 6px 18px rgba(0,0,0,0.18);
  }
  .card--contact { top: 70px; display: flex; }
  .card--logo { top: 470px; background: var(--sky-deep); }

  /* contact side */
  .brand-panel {
    width: 240px; height: 100%;
    background: var(--card-white);
    display: flex; align-items: center; justify-content: center;
  }
  .brand-name {
    font-family: "Exo 2", sans-serif; font-weight: 700;
    color: var(--ink); text-transform: uppercase;
    text-align: center; line-height: 1.1;
  }
  .brand-panel .brand-name { font-size: 26px; }
  .details-panel {
    flex: 1; position: relative;
    background:
      radial-gradient(circle at 12% 6%, #ffffff 0, var(--sky-light) 10%, rgba(85,189,240,0) 45%),
      linear-gradient(160deg, var(--sky-mid), var(--sky-deep));
  }
  .name-pill {
    position: absolute; top: 72px; left: 30px; right: -40px; height: 64px;
    border-radius: 32px 0 0 32px;
    background: linear-gradient(var(--pill-top), var(--pill-bottom));
    box-shadow: 0 3px 6px rgba(0,0,0,0.25);
    display: flex; align-items: center; padding-left: 34px;
  }
  .person-name {
    font-family: "Exo 2", sans-serif; font-weight: 700;
    font-size: 34px; letter-spacing: 2px; color: var(--ink);
    text-transform: uppercase; word-spacing: 8px;
  }
  .contact-list {
    position: absolute; left: 64px; top: 170px;
    list-style: none;
    font-family: "Open Sans", sans-serif; font-weight: 700;
    font-size: 17px; line-height: 29px;
    color: var(--contact-text);
  }

  /* logo side */
  .logo-band {
    position: absolute; left: 0; right: 0; top: 70px; height: 190px;
    background: var(--card-white);
    display: flex; align-items: center; justify-content: center;
    padding-left: 90px;
  }
  .card--logo::before {
    content: ""; position: absolute; inset: 0;
    background:
      radial-gradient(circle at 10% 20%, #ffffff 0, var(--sky-light) 8%, rgba(85,189,240,0) 40%),
      linear-gradient(165deg, var(--sky-mid), var(--sky-deep));
  }
  .logo-band .brand-name { font-size: 46px; }
</style>
</head>
<body>
<main class="canvas">
  <section class="card card--contact" aria-label="Business card, contact side">
    <div class="brand-panel">
      <p class="brand-name">Loft Pictures<br>Australia</p>
    </div>
    <div class="details-panel">
      <div class="name-pill"><h1 class="person-name">Ned Harrow</h1></div>
      <ul class="contact-list">
        <li>phone: 03 5521 4736</li>
        <li>Mobile: 0431 957 284</li>
        <li>email: ned@loftpicturez.example</li>
        <li>web: www.loftpictures.example</li>
      </ul>
    </div>
  </section>

  <section class="card card--logo" aria-label="Business card, brand side">
    <div class="logo-band">
      <p class="brand-name">Loft Pictures<br>Australia</p>
    </div>
  </section>
</main>
</body>
</html>
```